Wendrows Accountants and Tax Agents Practice

We need an update on our logo.
We require Letterhead, withcomp slips, and business cards for three partners
We currently have a logo and which is used on our letterheads but we need a much more professional and updated more modern version.
We are an Accounting Practice which needs upating. I will up load what we currently use and please use the all the wording and what another designer has proposed but need it to be different .
The colour scheme needs to be deep charcoal and a deep blue/green(065A7F) .

Target Market(s)

Individuals, companies, partnerships

Industry/Entity Type

Accounting

Font styles to use
Other font styles liked:
• ITC Avant Garde Gothic.

Colors
0393ce

Requirements
Must have
• Please follow the letter head upload the colour code and the colour charcoal.
• I would like the word Wendrows in bold Accountants (not bold) the font to be ITC Avant Garde Gothic.
• The business cards for all three partners need to have two sides the solid colour on one side with the name Wendrows Accountants. The other side with the name and details ( below details for each partner) Dorian Fellbracke FCPA, Gerald Trumbleton FCPA
• Martin Osgood (Blue/green) the T, F, E, W ( blue green) the rest in charcoal with white background
• FCPA
• 2718 Park Road Malvern VIC 3144
• T +61 3 94827713
• F + 61 9482 7159
• E martin@wendrows-example.com.au
• W wendrowsaccountants-example.com.au
• the letter faded letter G on the white side of the card in the top RH corner
Nice to have
• the letter G on the white side of the business card in shades of charcoal very faint
• Instead of E: for email using symbols for the details eg:✉

```html
<!DOCTYPE html>
<html lang="en">
<head>
<meta charset="utf-8">
<title>Wendrows Accountants – Business Card</title>
<link rel="stylesheet" href="https://fonts.googleapis.com/css2?family=Jost:wght@400;600&display=swap">
<style>
  :root {
    --blue-green: #065a7f;
    --blue-green-light: #0a7c9e;
    --charcoal: #3c3d3f;
    --charcoal-deep: #2c2d2f;
    --paper: #ffffff;
    --backdrop: #3a3a3b;
    --rule: #b9c4ca;
  }
  * { margin: 0; padding: 0; box-sizing: border-box; }
  html, body {
    width: 1200px; height: 674px; overflow: hidden;
    background: var(--backdrop);
    font-family: "Jost", "Helvetica Neue", Arial, sans-serif;
  }
  .canvas {
    position: relative; width: 1200px; height: 674px;
  }
  .card {
    position: absolute; top: 188px;
    width: 520px; height: 298px;
    overflow: hidden;
  }
  /* Front side */
  .card-front {
    left: 50px;
    background: linear-gradient(135deg, var(--blue-green) 0%, var(--blue-green-light) 100%);
  }
  .card-front .wordmark {
    position: absolute; left: 118px; top: 112px;
    color: var(--paper);
  }
  .wordmark {
    font-weight: 600; line-height: 1; letter-spacing: -0.5px;
  }
  .wordmark .name { display: block; font-size: 44px; }
  .wordmark .descriptor {
    display: block; font-size: 12.5px; letter-spacing: 3.4px;
    text-transform: uppercase; margin-top: 3px; padding-left: 70px;
  }
  /* Back side */
  .card-back {
    left: 630px;
    background: var(--paper);
  }
  .card-back .wordmark {
    position: absolute; left: 34px; top: 34px;
    color: var(--blue-green);
  }
  .card-back .wordmark .name { font-size: 34px; }
  .card-back .wordmark .descriptor { font-size: 10px; letter-spacing: 2.6px; padding-left: 54px; }
  .holder {
    position: absolute; left: 34px; top: 106px;
    font-weight: 400; font-size: 13.5px; letter-spacing: 0.6px;
    color: var(--blue-green); text-transform: uppercase;
  }
  .contacts {
    position: absolute; left: 34px; top: 132px;
    display: flex; gap: 9px;
  }
  .contact-icons {
    display: flex; flex-direction: column; gap: 3px;
    padding-right: 8px; border-right: 1px solid var(--rule);
  }
  .contact-icons svg { width: 11px; height: 13px; display: block; }
  .contact-lines {
    list-style: none; font-size: 11.5px; line-height: 16px; color: var(--charcoal);
  }
  .address {
    position: absolute; left: 34px; top: 206px;
    font-size: 11.5px; color: var(--charcoal);
  }
  .base-band {
    position: absolute; left: 0; bottom: 0; width: 100%; height: 11px;
    display: flex;
  }
  .base-band .band-blue { flex: 0 0 72%; background: var(--blue-green); }
  .base-band .band-gap { flex: 0 0 1%; background: var(--paper); }
  .base-band .band-charcoal { flex: 1; background: var(--charcoal-deep); }
</style>
</head>
<body>
<main class="canvas">
  <section class="card card-front" aria-label="Business card front">
    <div class="wordmark">
      <span class="name">Wendrows</span>
      <span class="descriptor">Accountants</span>
    </div>
  </section>

  <section class="card card-back" aria-label="Business card back">
    <div class="wordmark">
      <span class="name">Wendrows</span>
      <span class="descriptor">Accountants</span>
    </div>
    <p class="holder">Martin Osgood, FCPA</p>
    <div class="contacts">
      <div class="contact-icons" aria-hidden="true">
        <svg viewBox="0 0 12 14"><path d="M3 1.5 L5 4.5 L3.8 5.8 C4.5 7.6 5.6 8.9 7.2 9.8 L8.5 8.6 L11 10.6 L9.6 12.6 C5 12 1.4 7.4 1.2 2.8 Z" fill="var(--blue-green)"/></svg>
        <svg viewBox="0 0 12 14"><rect x="2" y="5" width="8" height="6" rx="1" fill="var(--blue-green)"/><rect x="3.5" y="2" width="5" height="3" fill="none" stroke="var(--blue-green)" stroke-width="1"/></svg>
        <svg viewBox="0 0 12 14"><rect x="1" y="3.5" width="10" height="7" rx="1" fill="none" stroke="var(--blue-green)" stroke-width="1.1"/><path d="M1.5 4 L6 7.8 L10.5 4" fill="none" stroke="var(--blue-green)" stroke-width="1.1"/></svg>
        <svg viewBox="0 0 12 14"><circle cx="6" cy="7" r="4.6" fill="none" stroke="var(--blue-green)" stroke-width="1.1"/><path d="M1.4 7 H10.6 M6 2.4 C4 5 4 9 6 11.6 M6 2.4 C8 5 8 9 6 11.6" fill="none" stroke="var(--blue-green)" stroke-width="0.9"/></svg>
      </div>
      <ul class="contact-lines">
        <li>+61 3 94827713</li>
        <li>+ 61 9482 7159</li>
        <li>martin@wendrows-example.com.au</li>
        <li>wendrowsaccountants-example.com.au</li>
      </ul>
    </div>
    <p class="address">2718 Park Road Malvern VIC 3144</p>
    <div class="base-band" aria-hidden="true">
      <span class="band-blue"></span><span class="band-gap"></span><span class="band-charcoal"></span>
    </div>
  </section>
</main>
</body>
</html>
```